We need a website design for an HVAC (Heating & Air Conditioning) Contractor*

Our HVAC client would like to have a more professional looking site as their current one (https://brindlecoolingworks.example/) is a template site. We will be building the site in-house from the concept.
Items we'd like to incorporate:
- A banner on the homepage that has a click to call plus a form on the right side of the banner
- There is a video on the current website homepage, please find a place to incorporate this.
- We will need to have at least 800 words of content on the homepage, please find space for that (can be a description of a few of the heating / air conditioning services they do). Feel free to use filler content (lorem ipsum) if need be to just show how the content would look

All submissions must have a homepage and a related subpage concept.

```html
<!DOCTYPE html>
<html lang="en">
<head>
<meta charset="utf-8">
<title>Brindle Cooling Works — Heat &amp; Air Conditioning</title>
<link href="https://fonts.googleapis.com/css2?family=Oswald:wght@400;500;600&family=Open+Sans:ital,wght@0,400;0,600;0,700;1,400&display=swap" rel="stylesheet">
<style>
:root{
  --red:#d0121b;
  --blue:#1c4b88;
  --navy:#163d6d;
  --deep:#123560;
  --pale:#eef2f7;
  --ice:#e4edf7;
  --ink:#1b2a3d;
  --grey:#6b7480;
  --white:#fff;
}
*{box-sizing:border-box;margin:0;padding:0}
html,body{width:1200px;height:4858px;overflow:hidden}
body{position:relative;font-family:"Open Sans",sans-serif;color:var(--ink);background:var(--white)}
section,header,footer{position:absolute;left:0;width:1200px;overflow:hidden}
.abs{position:absolute}
.h{font-family:"Oswald",sans-serif;font-weight:500;text-transform:uppercase}
.red{color:var(--red)}.blue{color:var(--navy)}
.ph{position:absolute}
.btn{position:absolute;display:flex;align-items:center;justify-content:center;font-family:"Oswald",sans-serif;font-weight:600;font-size:13px;letter-spacing:2px;text-transform:uppercase}
.btn-navy{background:var(--navy);color:#fff;box-shadow:4px 4px 0 var(--red)}
.btn-white{background:#fff;color:var(--navy);box-shadow:4px 4px 0 #c4c9d2}
.btn-red{background:var(--red);color:#fff}
p.copy{font-size:14px;line-height:23px;color:var(--grey)}

/* header */
.site-header{top:0;height:117px;background:#fff}
.brand{left:47px;top:26px;font-family:"Oswald",sans-serif;font-weight:600;font-size:30px;color:var(--red);text-transform:uppercase;display:flex;align-items:center;gap:10px;line-height:1}
.brand i{width:14px;height:14px;background:var(--red);display:block}
.topbar{left:764px;top:0;width:436px;height:38px;background:var(--navy);display:flex}
.topbar .social{display:flex;gap:22px;align-items:center;padding-left:34px;width:198px}
.topbar .social span{width:12px;height:12px;border-radius:50%;background:#fff;opacity:.9}
.topbar .call{flex:1;background:var(--red);color:#fff;font-family:"Oswald",sans-serif;font-size:19px;display:flex;align-items:center;justify-content:center;gap:8px}
.nav{left:474px;top:70px;display:flex;gap:52px;font-family:"Oswald",sans-serif;font-size:15px;color:var(--navy)}
.nav a{position:relative;text-decoration:none;color:inherit}
.nav a.on{color:var(--red)}
.nav a.on::after{content:"";position:absolute;left:-6px;right:-6px;top:40px;height:3px;background:var(--red)}

/* hero */
.hero{top:117px;height:615px;background:linear-gradient(180deg,#1e57a0,#1c4b88)}
.hero .skyline{left:0;bottom:0;width:1200px;height:200px;background:linear-gradient(180deg,rgba(22,61,109,0),rgba(22,61,109,.7))}
.hero-title{left:109px;top:162px;color:#fff;font-size:48px;line-height:56px}
.hero-title .band{position:absolute;left:-30px;top:10px;width:640px;height:28px}
.hero-title span{position:relative}
.hero-sub{left:109px;top:284px;width:480px;color:#fff;font-size:14px;line-height:22px}
.van-hero{left:211px;top:408px;width:483px;height:207px;border-radius:30px 60px 10px 10px;background:linear-gradient(90deg,#f2f4f8,#d6dce6)}
.enquiry{left:751px;top:94px;width:428px;height:412px;background:var(--navy);padding:28px 32px 0;color:#fff;text-align:center}
.enquiry h2{font-family:"Oswald",sans-serif;font-weight:500;font-size:25px}
.enquiry .lead{font-size:12px;margin:6px 0 16px}
.field{background:#fff;height:32px;margin:0 0 10px;color:#6b7480;font-size:11px;text-align:left;display:flex;align-items:center;gap:8px;padding-left:10px}
.field b{width:11px;height:11px;border:1px solid #8a93a0;border-radius:50%;display:block}
.field.msg{height:66px;align-items:flex-start;padding-top:9px}
.enquiry .send{position:static;height:34px;margin-top:14px}

/* about */
.about{top:732px;height:513px}
.about-photo{left:117px;top:113px;width:500px;height:314px;background:linear-gradient(135deg,#c9ced6,#8e96a3)}
.play{left:117px;top:381px;width:64px;height:46px;background:var(--red);display:flex;align-items:center;justify-content:center}
.about h2{left:674px;top:104px;font-size:44px;line-height:1}
.about .sub{left:674px;top:158px;font-family:"Oswald",sans-serif;font-size:23px;letter-spacing:4px;color:var(--ink)}
.about p{left:674px;top:212px;width:430px}

/* services */
.services{top:1245px;height:836px;background:var(--pale)}
.eyebrow{width:1200px;left:0;text-align:center;font-family:"Oswald",sans-serif;letter-spacing:4px;font-size:17px;color:var(--ink)}
.sec-title{width:1200px;left:0;text-align:center;font-size:40px}
.card{top:163px;width:485px;height:579px}
.card .img{height:296px}
.card.ac{left:106px;background:var(--red)}
.card.heat{left:615px;background:var(--navy)}
.card h3{position:absolute;left:38px;top:348px;color:#fff;font-family:"Oswald",sans-serif;font-weight:500;font-size:26px;text-transform:uppercase}
.card p{position:absolute;left:38px;top:392px;width:410px;color:#fff;font-size:11.5px;line-height:19.5px}
.card .btn{left:38px;top:515px;width:134px;height:34px;font-size:11px}

/* specialise */
.special{top:2081px;height:755px}
.ring{left:0;top:0}
.spec-van{left:151px;top:519px;width:374px;height:146px;border-radius:24px 60px 8px 8px;background:linear-gradient(90deg,#f2f4f8,#d4dae4)}
.item{position:absolute;display:flex;gap:22px;align-items:flex-start}
.item .ic{width:76px;height:76px;border-radius:50%;background:#fff;box-shadow:0 3px 12px rgba(0,0,0,.14);flex:none;display:flex;align-items:center;justify-content:center}
.item h4{font-family:"Oswald",sans-serif;font-weight:400;letter-spacing:3px;font-size:17px;margin-top:8px}
.item p{font-size:11.5px;line-height:18px;color:var(--grey);width:440px;margin-top:6px}

/* energy */
.energy{top:2836px;height:528px;background:var(--ice)}
.energy h2{left:113px;top:98px;font-size:34px;line-height:42px}
.energy .text{left:113px;top:200px;width:450px}
.energy .text p{font-size:12.5px;line-height:25px;color:#4a5461;margin-bottom:10px}

/* testimonials */
.testi{top:3364px;height:519px;background:var(--blue)}
.testi .kicker{left:117px;top:142px;color:#fff;font-family:"Oswald",sans-serif;letter-spacing:2px;font-size:16px}
.testi h2{left:117px;top:168px;color:#fff;font-size:34px;line-height:44px}
.testi .btn{left:117px;top:274px;width:175px;height:34px;font-size:12px}
.van-testi{left:72px;top:369px;width:409px;height:150px;border-radius:24px 60px 8px 8px;background:linear-gradient(90deg,#f2f4f8,#d4dae4)}
.quote{top:129px;width:302px;height:234px;background:#fff;border-bottom:5px solid var(--red);padding:30px 32px 0}
.quote p{font-style:italic;font-size:11.5px;line-height:21px;color:#5a6470}
.who{display:flex;gap:12px;align-items:center;margin-top:24px}
.who .av{width:30px;height:30px;border-radius:50%;background:#b8c0cc}
.who b{font-size:11px;display:block}
.stars{color:#f5b400;font-size:14px;letter-spacing:2px}

/* timely */
.timely{top:3883px;height:428px}
.timely-photo{left:104px;top:70px;width:449px;height:358px;background:linear-gradient(135deg,#dfe4ea,#3b7fd0)}
.timely h2{left:613px;top:118px;font-size:36px}
.timely p{left:613px;top:186px;width:520px;font-size:14px;line-height:26px;color:#4a5461}
.timely .btn{left:623px;top:265px;width:285px;height:47px;font-size:14px}

/* partners */
.partners{top:4311px;height:91px;display:flex;justify-content:space-around;align-items:center;padding:0 120px}
.partners span{width:130px;height:30px;background:#c6cbd2;border-radius:6px}

/* footer */
.site-footer{top:4402px;height:456px;background:var(--navy);color:#fff}
.site-footer h3{position:absolute;top:75px;font-family:"Oswald",sans-serif;font-weight:500;font-size:21px}
.links{position:absolute;top:130px;list-style:none;font-size:13px;line-height:26px}
.fsocial{left:142px;top:306px;display:flex;gap:28px}
.fsocial span{width:13px;height:13px;background:#fff;border-radius:50%;display:block}
.map{left:496px;top:117px;width:302px;height:193px;background:linear-gradient(135deg,#f1f2f4,#d9dce1)}
.contact{position:absolute;left:870px;display:flex;gap:18px}
.contact b{display:block;font-size:12px;font-weight:700;letter-spacing:1px}
.contact span{font-size:12.5px;line-height:22px}
.bottom{left:0;top:387px;width:1200px;border-top:1px solid rgba(255,255,255,.25);height:69px;font-size:11.5px}
</style>
</head>
<body>

<header class="site-header">
  <div class="abs brand"><i></i>Brindle Cooling Works</div>
  <div class="abs topbar">
    <div class="social"><span></span><span></span><span></span><span></span></div>
    <div class="call">
      <svg width="18" height="18" viewBox="0 0 24 24" fill="none" stroke="#fff" stroke-width="2"><path d="M5 3h4l2 5-3 2a12 12 0 0 0 6 6l2-3 5 2v4a2 2 0 0 1-2 2A18 18 0 0 1 3 5a2 2 0 0 1 2-2z"/></svg>
      (555) 014-2290
    </div>
  </div>
  <nav class="abs nav">
    <a class="on" href="#">HOME</a><a href="#">ABOUT US</a><a href="#">SERVICES</a><a href="#">TESTIMONIALS</a><a href="#">SPECIALS</a><a href="#">CONTACT US</a>
  </nav>
</header>

<section class="hero">
  <div class="abs skyline" role="img" aria-label="City skyline silhouette in blue tones"></div>
  <h1 class="abs h hero-title">
    <svg class="band" viewBox="0 0 640 28" preserveAspectRatio="none"><polygon points="0,20 30,0 600,0 600,-8 640,14 600,36 600,28 0,28" fill="#d0121b"/><polygon points="0,28 30,8 620,8 620,12 30,12 6,28" fill="#fff"/></svg>
    <span>Keep your friends and<br>family comfortable</span>
  </h1>
  <p class="abs hero-sub">WE NOW OFFER A FULL LINE OF SANITATION SERVICES TO COMBAT COVID-19! ASK US ABOUT THESE SERVICES TODAY!</p>
  <a class="btn btn-red" style="left:109px;top:351px;width:161px;height:38px">Contact us</a>
  <div class="ph van-hero" role="img" aria-label="Company service van with branding and phone number"></div>
  <form class="abs enquiry">
    <h2>ENQUIRY FORM</h2>
    <div class="lead">Get free quote now from our expert</div>
    <div class="field"><b></b>Your Name</div>
    <div class="field"><b></b>Email Address</div>
    <div class="field"><b></b>Phone Number</div>
    <div class="field"><b></b>Contact Prefer time</div>
    <div class="field msg"><b></b>Your Message</div>
    <div class="btn btn-red send">Send message</div>
  </form>
</section>

<section class="about">
  <div class="ph about-photo" role="img" aria-label="Family relaxing together on the living room floor (video thumbnail)"></div>
  <div class="abs play"><svg width="18" height="20" viewBox="0 0 18 20"><polygon points="0,0 18,10 0,20" fill="#fff"/></svg></div>
  <h2 class="abs h"><span class="red">About</span> <span class="blue">Brindle</span></h2>
  <div class="abs sub">HEAT &amp; AIR CONDITIONING</div>
  <p class="abs copy">Lorem ipsum dolor sit amet, consectetur adipiscing elit, sed do eiusmod tempor incididunt ut labore et dolore magna aliqua. Ut enim ad minim veniam, quis nostrud exercitation ullamco laboris nisi ut aliquip ex ea commodo consequat. Duis aute irure dolor in reprehenderit in voluptate velit esse cillum dolore eu fugiat nulla pariatur. Excepteur sint occaec</p>
  <a class="btn btn-navy" style="left:675px;top:381px;width:155px;height:38px">Learn more</a>
</section>

<section class="services">
  <div class="abs eyebrow" style="top:50px">WHAT WE DO</div>
  <h2 class="abs h sec-title" style="top:72px"><span class="red">Our</span> <span class="blue">Services</span></h2>
  <article class="abs card ac">
    <div class="img" role="img" aria-label="Technician repairing a wall-mounted air conditioner" style="background:linear-gradient(135deg,#e8e4e0,#9aa6b6)"></div>
    <h3>AC Repair</h3>
    <p>Lorem ipsum dolor sit amet, consectetur adipiscing elit, sed do eiusmod tempor incididunt ut labore et dolore magna aliqua. Ut enim ad minim veniam, quis nostrud exercitation ullamco laboris nisi ut aliquip ex ea commodo consequat. Duis aute irure dolor in reprehenderit in Lorem ipsum dolor sit amet, consectetur adipiscing elit, sed do eiusmod tempor incididunt ut labore et dolore magna aliqua. Ut enim ad minim</p>
    <a class="btn btn-white">Learn more</a>
  </article>
  <article class="abs card heat">
    <div class="img" role="img" aria-label="Technician servicing a heating boiler" style="background:linear-gradient(135deg,#2a5d9e,#d8dde4)"></div>
    <h3>About Heating</h3>
    <p>Lorem ipsum dolor sit amet, consectetur adipiscing elit, sed do eiusmod tempor incididunt ut labore et dolore magna aliqua. Ut enim ad minim veniam, quis nostrud exercitation ullamco laboris nisi ut aliquip ex ea commodo consequat. Duis aute irure dolor in reprehenderit in Lorem ipsum dolor sit amet, consectetur adipiscing elit, sed do eiusmod tempor incididunt ut labore et dolore magna aliqua. Ut enim ad minim</p>
    <a class="btn btn-white">Learn more</a>
  </article>
</section>

<section class="special">
  <div class="abs eyebrow" style="top:48px">WHY WE ARE</div>
  <h2 class="abs h sec-title" style="top:70px"><span class="red">Specialise</span> <span class="blue">Services</span></h2>
  <svg class="ring" width="640" height="755">
    <circle cx="343" cy="410" r="220" fill="#fff" stroke="#e2e6ec" stroke-width="2"/>
    <circle cx="343" cy="410" r="185" fill="#1c4b88"/>
    <path d="M343 190 A220 220 0 0 1 343 630" fill="none" stroke="#cfd5dd" stroke-width="2"/>
    <circle cx="491" cy="245" r="6" fill="#d0121b"/>
    <circle cx="551" cy="335" r="6" fill="#d0121b"/>
    <circle cx="563" cy="432" r="6" fill="#d0121b"/>
    <circle cx="531" cy="528" r="6" fill="#d0121b"/>
    <text x="343" y="420" text-anchor="middle" font-family="Oswald,sans-serif" font-size="40" font-weight="600" fill="#fff">BRINDLE</text>
  </svg>
  <div class="ph spec-van" role="img" aria-label="Company service van"></div>
  <div class="item" style="left:519px;top:168px"><div class="ic"><svg width="34" height="34" viewBox="0 0 34 34" fill="none" stroke="#d0121b" stroke-width="2"><rect x="4" y="8" width="26" height="16"/><path d="M8 28v-4M26 28v-4M10 14h14"/></svg></div><div><h4>HVAC REPAIR</h4><p>Lorem ipsum dolor sit amet, consectetur adipiscing elit, sed do eiusmod tempor incididunt ut labore et dolore magna aliqua. Ut enim ad minim veniam</p></div></div>
  <div class="item" style="left:594px;top:285px"><div class="ic"><svg width="34" height="34" viewBox="0 0 34 34" fill="none" stroke="#d0121b" stroke-width="2"><rect x="5" y="12" width="24" height="16"/><path d="M9 12V6M17 12V6M25 12V6M5 20h24"/></svg></div><div><h4>GEOTHERMAL</h4><p style="width:370px">Lorem ipsum dolor sit amet, consectetur adipiscing elit, sed do eiusmod tempor incididunt ut labore et dolore magna</p></div></div>
  <div class="item" style="left:605px;top:402px"><div class="ic"><svg width="34" height="34" viewBox="0 0 34 34" fill="none" stroke="#d0121b" stroke-width="2"><rect x="5" y="10" width="24" height="18"/><path d="M13 10V6h8v4M5 18h24"/></svg></div><div><h4>COMMERCIAL REPAIRS</h4><p style="width:380px">Lorem ipsum dolor sit amet, consectetur adipiscing elit, sed do eiusmod tempor incididunt ut labore et dolore magna aliqua.</p></div></div>
  <div class="item" style="left:562px;top:523px"><div class="ic"><svg width="34" height="34" viewBox="0 0 34 34" fill="none" stroke="#d0121b" stroke-width="2"><rect x="5" y="6" width="24" height="22"/><path d="M9 12h16M9 18h10M9 24h6"/></svg></div><div><h4>MAINTENANCE &amp; INSTALL</h4><p>Lorem ipsum dolor sit amet, consectetur adipiscing elit, sed do eiusmod tempor incididunt ut labore et dolore magna aliqua. Ut enim</p></div></div>
</section>

<section class="energy">
  <svg class="abs" style="left:0;top:0" width="1200" height="528"><polygon points="774,0 1200,0 1200,528 491,528" fill="#2c62a6" role="img" aria-label="Technician working on a manifold of pipes and valves"/></svg>
  <h2 class="abs h"><span class="red">Go the energy</span><br><span class="blue">efficient route</span></h2>
  <div class="abs text">
    <p>Brindle Cooling Works, LLC provides a wide variety of residential and commercial HVAC services in the Fenwick, OK area.</p>
    <p>With over a decade of experience, you can trust our HVAC company to install, repair and maintain the HVAC systems in your home or commercial building. Our technician can find out what's wrong with your malfunctioning heating or cooling system and repair or replace it on the spot. We specialize in energy-efficient geothermal heating</p>
  </div>
  <a class="btn btn-navy" style="left:113px;top:383px;width:153px;height:40px">Learn more</a>
</section>

<section class="testi">
  <svg class="abs" style="left:0;top:0" width="420" height="519"><polygon points="0,0 406,0 0,519" fill="#d0121b"/></svg>
  <div class="abs kicker">TESTIMONIALS</div>
  <h2 class="abs h">What our<br>customer says</h2>
  <a class="btn btn-white">View all reviews</a>
  <div class="ph van-testi" role="img" aria-label="Company service van"></div>
  <div class="abs quote" style="left:453px"><p>"Lorem ipsum dolor sit amet, consectetur adipiscing elit, sed do eiusmod tempor incididunt ut labore et dolore magna aliqua. Ut enim ad aliqua. Ut enim ad minim veniam, quis nostrud exercitation"</p><div class="who"><div class="av"></div><div><b>DANA HOLLOWAY</b><span class="stars">★★★★★</span></div></div></div>
  <div class="abs quote" style="left:796px"><p>"Lorem ipsum dolor sit amet, consectetur adipiscing elit, sed do eiusmod tempor incididunt ut labore et dolore magna aliqua. Ut enim ad aliqua. Ut enim ad minim veniam, quis nostrud exercitation"</p><div class="who"><div class="av"></div><div><b>DANA HOLLOWAY</b><span class="stars">★★★★★</span></div></div></div>
</section>

<section class="timely">
  <div class="ph timely-photo" role="img" aria-label="Technician with gauges beside an outdoor condenser unit"></div>
  <h2 class="abs h"><span class="red">Timely. Honest.</span> <span class="blue">Professional.</span></h2>
  <p class="abs">Brindle Cooling Works installs energy-efficient geothermal heating and cooling systems. We proudly serve the communities of:</p>
  <a class="btn btn-navy">Schedule an appointment</a>
</section>

<section class="partners" aria-label="Communities served">
  <span></span><span></span><span></span><span></span><span></span><span></span>
</section>

<footer class="site-footer">
  <h3 style="left:142px">NAVIGATION</h3>
  <ul class="links" style="left:142px"><li>Home</li><li>About Us</li><li>Our Services</li><li>Special</li><li>HVAC Installation</li><li>Maintenance Plan</li></ul>
  <ul class="links" style="left:325px;top:133px"><li>Hearth Financing</li><li>Testimonials</li><li>Career</li><li>Geo Thermal</li><li>Terms of Use</li></ul>
  <div class="abs fsocial"><span></span><span></span><span></span><span></span></div>
  <h3 style="left:494px">OUR LOCATION</h3>
  <div class="ph map" role="img" aria-label="Street map showing the office location"></div>
  <svg class="abs" style="left:630px;top:187px" width="26" height="34" viewBox="0 0 26 34"><path d="M13 0a13 13 0 0 0-13 13c0 10 13 21 13 21s13-11 13-21A13 13 0 0 0 13 0z" fill="#d0121b"/><circle cx="13" cy="13" r="5" fill="#fff"/></svg>
  <h3 style="left:870px">CONTACT US</h3>
  <div class="contact" style="top:120px"><svg width="26" height="30" viewBox="0 0 26 34"><path d="M13 2a11 11 0 0 0-11 11c0 9 11 19 11 19s11-10 11-19A11 11 0 0 0 13 2z" fill="#fff"/><circle cx="13" cy="13" r="4" fill="#163d6d"/></svg><div><b>ADDRESS</b><span>FENWICK, OK 70010</span></div></div>
  <div class="contact" style="top:190px"><svg width="28" height="28" viewBox="0 0 24 24" fill="none" stroke="#fff" stroke-width="1.6"><path d="M5 3h4l2 5-3 2a12 12 0 0 0 6 6l2-3 5 2v4a2 2 0 0 1-2 2A18 18 0 0 1 3 5a2 2 0 0 1 2-2z"/></svg><div><b>PHONE NUMBER</b><span>(555) 014-2290</span></div></div>
  <div class="contact" style="top:255px"><svg width="28" height="28" viewBox="0 0 24 24" fill="none" stroke="#fff" stroke-width="1.6"><circle cx="12" cy="12" r="10"/><path d="M7 12l4 4 7-8"/></svg><div><b>WORKING HOURS</b><span>Mon- Fri: 7:00 Am to 9:00 Pm<br>Sat-Sun: 8:00 Am to 5:00 Pm</span></div></div>
  <div class="abs bottom">
    <span class="abs" style="left:136px;top:26px">© 2020 Brindle Cooling Works  All Rights Reserved.</span>
    <span class="abs" style="left:918px;top:30px">Policy Privacy &nbsp;|&nbsp; Terms of Use</span>
  </div>
</footer>

</body>
</html>
```